Create an awesome website for a medical clinic

This is a new website for a doctor's office. The site should be clean and modern, easy to navigate.

This is a wellness clinic, we want to help our clients have a healthy, active lifestyle. It should be friendly and inviting, and easy for them to call or schedule an appointment.

The site should be responsive and designed using the attached Bootstrap 3 PSD.

We will provide stock photos, until then please use stock photos from:

photoharvestbin.net or
lumapicturevault.net (preferred)

Some example sites of clean and modern designs that we like:

https://tarnelspine.example/
http://walkpastjoints.example/
http://feelingbrisker.example/

Also attached is a temporary logo you can use.
Updates

Reason: Thank you everyone for your great designs - we need a little more time so I'm extending the project.

Need extra days to review

Also, the colors in the new logo I just linked to are the final colors of the logo, so feel free to use any complimentary colors to it.

Hi everyone, The boss wants to change the layout of the site a little bit - here's the revised layout: https://www.filecrate.example/s/q8vn31kd2pxe74rt/memo%2011_29_2017.pdf?dl=0 And the graphic assets you can use are here: https://www.filecrate.example/s/q8vn31kd2pxe74rt/memo%2011_29_2017.pdf?dl=0 Feel free to change the background color of the "topbar", and change the icons of the "why people trust us" if you want, these are just temporary placeholders. Thanks for your patience and hard work!

Target Market(s)

People seeking medical treatment (wellness clinic)

Industry/Entity Type

Doctor

Number of Pages Required

1 page

Font styles to use
Sans Serif

Colors
0592cd
33a6d7
abd037
9bcb3c

Requirements
Must have
• The home page should have: a strong hero image/slideshow, clinic phone number should be prominent and at the top of the page (in the nav), a "what to expect" section (this is like a FAQs section - see attachment), and a strong call to action (a button to call or schedule an appointment).
• The what to expect section is useful so that prospective clients can determine if we're a good fit for them or not. It's a basic, first-step pre-qualification block of information.
• Social media icons which links to our social media profiles should be included.
Nice to have
• - Link to 3 most recent blog entries
• - Testimonials
• - How a multilevel nav menu looks.

```html
<!DOCTYPE html>
<html lang="en">
<head>
<meta charset="utf-8">
<title>Wellness Clinic – Conditions</title>
<link href="https://fonts.googleapis.com/css2?family=Open+Sans:wght@400;600;700&display=swap" rel="stylesheet">
<style>
:root{
  --blue:#0592cd;
  --blue-light:#33a6d7;
  --green:#9bcb3c;
  --text:#3a3a3a;
  --frame:#d9d9d9;
  --white:#ffffff;
}
*{box-sizing:border-box;margin:0;padding:0}
html,body{width:960px;height:1200px;overflow:hidden}
body{font-family:"Open Sans",Arial,sans-serif;position:relative;background:var(--white);color:var(--text)}
.backdrop{position:absolute;inset:0;z-index:0}
.section-title{position:absolute;left:0;width:960px;text-align:center;font-weight:600;font-size:27px;color:var(--blue)}
.title-rule{position:absolute;left:192px;width:576px;height:3px;background:var(--blue)}
.conditions .section-title{top:26px}
.conditions .title-rule{top:68px}
.condition-card{position:absolute;width:194px;height:260px;
  background:linear-gradient(to bottom,rgba(255,255,255,0) 0%,rgba(255,255,255,0) 40%,#5db8e0 75%,var(--blue) 100%)}
.condition-frame{position:absolute;left:10px;top:0;width:175px;height:209px;background:var(--frame);padding:6px}
.condition-frame .art{width:100%;height:100%;border:0}
.condition-label{position:absolute;left:0;right:0;top:220px;text-align:center;color:var(--white);font-weight:600;font-size:18px}
.c1{left:131px;top:118px}.c2{left:383px;top:118px}.c3{left:635px;top:118px}
.c4{left:131px;top:411px}.c5{left:383px;top:411px}.c6{left:635px;top:411px}
.ready-panel{position:absolute;left:59px;top:737px;width:842px;height:329px;background:rgba(255,255,255,.72)}
.ready-panel .section-title{left:0;width:842px;top:14px}
.ready-panel .title-rule{left:133px;top:52px}
.ready-panel p{position:absolute;font-size:12.6px;line-height:16px}
.intro{left:51px;top:77px;width:760px}
.quote{left:53px;width:740px;border-left:2px solid var(--blue);padding-left:13px}
.q1{top:152px}.q2{top:213px}
.call-button{position:absolute;left:368px;top:273px;width:107px;height:30px;border-radius:3px;background:var(--blue);
  color:var(--white);font-weight:700;font-size:11.5px;text-align:center;line-height:30px;text-decoration:none}
.expect-band{position:absolute;left:0;top:1115px;width:960px;height:85px;background:var(--green)}
.expect-band .section-title{color:var(--white);top:10px}
.expect-band .title-rule{background:var(--white);top:50px}
</style>
</head>
<body>
<svg class="backdrop" width="960" height="1200" viewBox="0 0 960 1200" aria-hidden="true">
  <defs>
    <linearGradient id="sky" x1="0" y1="0" x2="1" y2="1">
      <stop offset="0" stop-color="#e6f4fa"/>
      <stop offset="0.55" stop-color="#9dd3ec"/>
      <stop offset="1" stop-color="#0592cd"/>
    </linearGradient>
  </defs>
  <rect width="960" height="1200" fill="url(#sky)"/>
  <ellipse cx="560" cy="360" rx="700" ry="770" fill="#ffffff" opacity="0.35"/>
  <ellipse cx="420" cy="190" rx="640" ry="760" fill="#ffffff"/>
</svg>

<section class="conditions">
  <h2 class="section-title">Do You Suffer From Any of the Following?</h2>
  <div class="title-rule"></div>

  <div class="condition-card c1"><div class="condition-frame"><svg class="art" role="img" aria-label="Illustration of a translucent head with the brain highlighted"><rect width="100%" height="100%" fill="#1f7bc4"/></svg></div><div class="condition-label">Headache</div></div>
  <div class="condition-card c2"><div class="condition-frame"><svg class="art" role="img" aria-label="Illustration of a figure from behind with neck and upper spine pain highlighted"><rect width="100%" height="100%" fill="#0b2440"/></svg></div><div class="condition-label">Headache</div></div>
  <div class="condition-card c3"><div class="condition-frame"><svg class="art" role="img" aria-label="Illustration of a figure holding the temple with a head pain point highlighted"><rect width="100%" height="100%" fill="#0c2747"/></svg></div><div class="condition-label">Headache</div></div>
  <div class="condition-card c4"><div class="condition-frame"><svg class="art" role="img" aria-label="Illustration of a skeleton from behind with lower back pain highlighted"><rect width="100%" height="100%" fill="#0d2a4e"/></svg></div><div class="condition-label">Headache</div></div>
  <div class="condition-card c5"><div class="condition-frame"><svg class="art" role="img" aria-label="Illustration of a figure touching the forehead with the brain visible"><rect width="100%" height="100%" fill="#123a66"/></svg></div><div class="condition-label">Headache</div></div>
  <div class="condition-card c6"><div class="condition-frame"><svg class="art" role="img" aria-label="Illustration of a skeleton with the cervical spine highlighted"><rect width="100%" height="100%" fill="#101e33"/></svg></div><div class="condition-label">Headache</div></div>
</section>

<section class="ready-panel">
  <h2 class="section-title">Are You Ready to Feel Better?</h2>
  <div class="title-rule"></div>
  <p class="intro">Lorem ipsum dolor sit amet, nostra in aliquet arcu leo eu, aliquet integer sed leo blandit, vivamus sollicitudin vel sagittis. Nesciunt nunc eu aliquet sodales enim scelerisque, explicabo amet quis. Amet tempor cras vitae, amet et ante. Consequat libero odio, lorem bibendum, pellentesque congue. Malesuada amet, amet nibh nulla justo mattis imperdiet in, wisi vero nibh incidunt posuere ligula, quibusdam sodales.</p>
  <p class="quote q1">Lorem ipsum dolor sit amet, nostra in aliquet arcu leo eu, aliquet integer sed leo blandit, vivamus sollicitudin vel sagittis. Nesciunt nunc eu aliquet sodales enim scelerisque, explicabo amet quis. Amet tempor cras vitae, amet et ante mattis imperdiet in, wisi vero nibh incidunt posuere ligula, quibusdam sodales.</p>
  <p class="quote q2">Lorem ipsum dolor sit amet, nostra in aliquet arcu leo eu, aliquet integer sed leo blandit, vivamus sollicitudin vel sagittis. Nesciunt nunc eu aliquet sodales enim scelerisque, explicabo amet quis. Amet tempor cras vitae, amet et ante mattis imperdiet in, wisi vero nibh incidunt posuere ligula, quibusdam sodales.</p>
  <a class="call-button" href="#">CALL US</a>
</section>

<section class="expect-band">
  <h2 class="section-title">What to Expect</h2>
  <div class="title-rule"></div>
</section>
</body>
</html>
```